Business card for different employees

A professional new updated design incorporating our current business's color themes and styles such as our on-site service trucks decals included in pictures attached. Our current business card is very simple and not professionally designed. We are a small family business but want a professional corporate look.

Target Market(s)

Cards to be handed out to new customers , corperate meetings. For our on site service operators.

Industry/Entity Type

Hydraulic

Contact Information for Business Card

Address, website, phone number, email, logo.
slogan - "Industry chosen hose and fittings provider".
24/7 on-site service , supply and hose management
Experienced , indpendant , family owned

Font styles to use
Sans Serif

Requirements
Must have
• Easily editable so that I can add different names and different roles for employees etc.
Nice to have
• Freedom with colour doesn't necessarily have to be blue but that is our company colour theme with trucks and logo so makes sense for the card to have blue like the trucks.

```html
<!DOCTYPE html>
<html lang="en">
<head>
<meta charset="utf-8">
<title>Meridian Hose and Fittings – Business Card</title>
<link rel="stylesheet" href="https://fonts.googleapis.com/css2?family=Open+Sans:wght@300;400;600&display=swap">
<style>
  :root {
    --page-bg: #ecebe8;
    --brand-blue: #2f47a6;
    --brand-blue-light: #3d58c0;
    --steel-dark: #3c424d;
    --steel-mid: #8d929b;
    --steel-light: #d9dbdf;
    --card-white: #ffffff;
    --ink: #2a2f3a;
    --ink-soft: #5a606b;
  }
  * { box-sizing: border-box; margin: 0; padding: 0; }
  html, body {
    width: 1200px; height: 1080px; overflow: hidden;
    background: var(--page-bg);
    font-family: "Open Sans", sans-serif;
  }
  .sheet {
    position: relative; width: 1200px; height: 1080px;
    display: flex; flex-direction: column; align-items: center;
    justify-content: center; gap: 60px;
  }
  .card {
    position: relative; width: 760px; height: 437px; overflow: hidden;
    box-shadow: 0 6px 18px rgba(0,0,0,0.18);
  }
  .card__art { position: absolute; inset: 0; width: 100%; height: 100%; }

  /* Front */
  .card--front { background: var(--brand-blue); color: var(--card-white); }
  .front-brand {
    position: absolute; left: 0; right: 0; top: 112px;
    display: flex; flex-direction: column; align-items: center;
  }
  .brand-lockup { display: flex; align-items: center; gap: 12px; }
  .brand-lockup__dot {
    width: 26px; height: 26px; border-radius: 50%; background: currentColor;
  }
  .brand-lockup__name {
    font-weight: 600; font-size: 24px; letter-spacing: 1px; text-transform: uppercase;
  }
  .front-brand__rule {
    width: 336px; height: 1px; background: rgba(255,255,255,0.85); margin-top: 18px;
  }
  .front-brand__slogan { margin-top: 8px; font-size: 17px; font-weight: 400; }
  .service-list {
    position: absolute; left: 0; right: 0; top: 688px; list-style: none;
  }
  .service-row {
    position: absolute; left: 0; right: 0; display: flex; justify-content: center;
    gap: 46px; list-style: none; font-size: 17px;
  }
  .service-row--one { top: 310px; padding-left: 20px; }
  .service-row--two { top: 360px; gap: 32px; }
  .service-row li { display: flex; align-items: center; gap: 22px; }
  .service-row li::before {
    content: ""; width: 3px; height: 18px; background: var(--card-white);
  }

  /* Back */
  .card--back { background: var(--card-white); color: var(--ink); }
  .staff { position: absolute; left: 83px; top: 92px; }
  .staff__name {
    font-weight: 300; font-size: 42px; letter-spacing: 7px; color: var(--ink);
  }
  .staff__role {
    margin-top: 4px; font-size: 13px; letter-spacing: 2.5px; color: var(--ink-soft);
  }
  .contact-list {
    position: absolute; left: 83px; top: 228px; list-style: none;
    font-size: 13px; color: var(--ink-soft);
  }
  .contact-list li { display: flex; align-items: center; gap: 22px; height: 46px; }
  .contact-list svg { width: 20px; height: 20px; fill: var(--ink); flex: none; }
  .card--back .brand-lockup {
    position: absolute; right: 30px; bottom: 46px; color: var(--brand-blue);
  }
  .card--back .brand-lockup__name { font-size: 21px; }
</style>
</head>
<body>
<main class="sheet">

  <section class="card card--front" aria-label="Business card front">
    <svg class="card__art" viewBox="0 0 760 437" preserveAspectRatio="none" aria-hidden="true">
      <defs>
        <linearGradient id="cornerSteel" x1="0" y1="0" x2="1" y2="1">
          <stop offset="0" stop-color="#5a6070"/>
          <stop offset="1" stop-color="#2a2e38"/>
        </linearGradient>
      </defs>
      <polygon points="330,0 470,0 150,437 10,437" fill="var(--brand-blue-light)" opacity="0.35"/>
      <polygon points="560,0 620,0 300,437 240,437" fill="var(--brand-blue-light)" opacity="0.3"/>
      <rect x="0" y="300" width="760" height="8" fill="#ffffff" opacity="0.06"/>
      <polygon points="760,365 760,437 580,437 640,365" fill="url(#cornerSteel)" opacity="0.9"/>
    </svg>

    <div class="front-brand">
      <div class="brand-lockup">
        <span class="brand-lockup__dot"></span>
        <span class="brand-lockup__name">Meridian Hose and Fittings</span>
      </div>
      <span class="front-brand__rule"></span>
      <p class="front-brand__slogan">Industry Chosen Hose &amp; Fittings Provider</p>
    </div>

    <ul class="service-row service-row--one">
      <li>24/7 on-site service</li>
      <li>Supply and hose management</li>
    </ul>
    <ul class="service-row service-row--two">
      <li>Experienced</li>
      <li>Indpendant</li>
      <li>Family Owned</li>
    </ul>
  </section>

  <section class="card card--back" aria-label="Business card back">
    <svg class="card__art" viewBox="0 0 760 437" preserveAspectRatio="none" aria-hidden="true">
      <defs>
        <linearGradient id="headSteel" x1="0" y1="0" x2="1" y2="1">
          <stop offset="0" stop-color="#2c313b"/>
          <stop offset="1" stop-color="#8d929b"/>
        </linearGradient>
        <linearGradient id="bandSoft" x1="0" y1="0" x2="1" y2="0">
          <stop offset="0" stop-color="#c8cbd0"/>
          <stop offset="1" stop-color="#f3f4f5"/>
        </linearGradient>
      </defs>
      <polygon points="0,0 270,0 190,82 0,82" fill="url(#headSteel)"/>
      <polygon points="280,0 340,0 250,82 190,82" fill="var(--steel-mid)" opacity="0.75"/>
      <polygon points="330,0 820,0 820,30 300,30" fill="var(--steel-light)" opacity="0.5"/>
      <polygon points="0,82 190,82 170,100 0,100" fill="var(--steel-light)"/>
      <polygon points="340,180 520,70 420,437 260,437" fill="url(#bandSoft)" opacity="0.7"/>
      <polygon points="150,437 400,200 460,200 230,437" fill="var(--steel-light)" opacity="0.6"/>
    </svg>

    <div class="staff">
      <h1 class="staff__name">YOUR NAME</h1>
      <p class="staff__role">YOUR POSITION</p>
    </div>

    <ul class="contact-list">
      <li>
        <svg viewBox="0 0 24 24" aria-hidden="true"><path d="M8 2h4l1 5-3 2a11 11 0 0 0 5 5l2-3 5 1v4a2 2 0 0 1-2 2A18 18 0 0 1 6 4a2 2 0 0 1 2-2z"/></svg>
        <span>+0400 555 129</span>
      </li>
      <li>
        <svg viewBox="0 0 24 24" aria-hidden="true"><path d="M2 5h20v14H2z M3 6l9 7 9-7v1.5l-9 7-9-7z" fill-rule="evenodd"/></svg>
        <span>info@meridianhose.com.au</span>
      </li>
      <li>
        <svg viewBox="0 0 24 24" aria-hidden="true"><path d="M12 2a7 7 0 0 0-7 7c0 5 7 13 7 13s7-8 7-13a7 7 0 0 0-7-7zm0 9.5a2.5 2.5 0 1 1 0-5 2.5 2.5 0 0 1 0 5z"/></svg>
        <span>Your Adress Line</span>
      </li>
    </ul>

    <div class="brand-lockup">
      <span class="brand-lockup__dot"></span>
      <span class="brand-lockup__name">Meridian Hose and Fittings</span>
    </div>
  </section>

</main>
</body>
</html>
```